Flyer-Design für Mittagsbelieferung
Zielgruppe
Mittags Belieferung ältere Menschen, Firmen, Berufstätige
Aufgabenstellung
Text aus Datei den Bestellzettel nicht weiter beachten nur Seite 2 u.3... Logo vielleicht vorne drauf... Format bin ich unentschieden

```html
<!DOCTYPE html>
<html lang="de">
<head>
<meta charset="utf-8">
<title>pilvo – Flyer Mittagstisch</title>
<link rel="stylesheet" href="https://fonts.googleapis.com/css2?family=Open+Sans:wght@400;600;700;800&family=Oswald:wght@500;600&display=swap">
<style>
  :root{
    --green:#3fa13a;
    --green-dark:#2f8a2c;
    --ink:#222;
    --paper:#ffffff;
    --backdrop:#e8e8ea;
  }
  *{box-sizing:border-box;margin:0;padding:0}
  html,body{width:938px;height:1200px;overflow:hidden}
  body{background:var(--backdrop);font-family:"Open Sans",Arial,sans-serif;color:var(--ink);position:relative}

  .flyer{position:absolute;left:39px;width:860px;height:560px;background:var(--paper);overflow:hidden;box-shadow:0 6px 18px rgba(0,0,0,.12)}
  .flyer--front{top:24px}
  .flyer--back{top:616px}

  /* FRONT */
  .front-photo{position:absolute;left:0;top:110px;width:500px;height:450px;
    clip-path:ellipse(100% 100% at 0% 100%);
    background:radial-gradient(circle at 40% 35%,#f08a4b 0 13%,transparent 14%),
               radial-gradient(circle at 62% 78%,#7cc63a 0 18%,transparent 19%),
               radial-gradient(circle at 22% 58%,#f3f1ec 0 15%,transparent 16%),
               radial-gradient(circle at 18% 22%,#7a5a3a 0 11%,transparent 12%),
               linear-gradient(135deg,#2f5e2a,#4a7a36 45%,#6fae3a)}
  .brand{position:absolute;right:40px;top:50px;width:420px;text-align:center}
  .brand__name{font-size:44px;font-weight:800;color:var(--green);line-height:1}
  .brand__tagline{font-size:19px;font-weight:700;margin-top:10px;white-space:nowrap}
  .front-phone{position:absolute;right:70px;top:260px;font-family:"Oswald",sans-serif;font-weight:600;font-size:40px;letter-spacing:1px;line-height:1}
  .front-mail{position:absolute;right:36px;top:420px;border:4px solid var(--green);border-radius:6px;padding:10px 20px;display:flex;align-items:center;gap:14px;font-size:26px;font-weight:700;white-space:nowrap}
  .price-badge{position:absolute;left:262px;top:340px;width:170px;height:170px;border-radius:50%;background:var(--green);
    box-shadow:0 0 0 5px var(--paper),0 0 0 9px var(--green);color:#fff;text-align:center;display:flex;flex-direction:column;justify-content:center;padding:16px}
  .price-badge__price{font-size:23px;font-weight:700;line-height:1.1}
  .price-badge__note{font-size:9px;margin-bottom:6px}
  .price-badge__extra{font-size:10px;font-weight:600;line-height:1.35}
  .price-badge__extra b{font-size:14px}

  /* BACK */
  .back-text{position:absolute;left:28px;top:36px;width:560px;font-size:14.5px;line-height:1.45}
  .back-text p{margin-bottom:8px}
  .hl{color:var(--green);font-weight:700}
  .payment{list-style:none;margin:2px 0 8px}
  .payment li{padding-left:18px;position:relative;margin-bottom:4px}
  .payment li::before{content:"✓";position:absolute;left:0;color:var(--green);font-weight:700}
  .area-band{background:var(--green);color:#fff;padding:8px 10px;margin:8px 0 10px;font-size:14.5px}
  .hotline{position:absolute;left:200px;top:478px;width:380px;text-align:center}
  .hotline__label{font-weight:700;font-size:15px;margin-bottom:6px}
  .hotline__row{display:flex;justify-content:center;gap:26px;font-weight:700;font-size:15px}
  .hotline__row span{display:flex;align-items:center;gap:6px}
  .back-brand{position:absolute;left:40px;top:488px;display:flex;align-items:center;gap:8px;font-weight:800;font-size:24px;color:var(--green)}
  .back-brand i{width:14px;height:14px;border-radius:50%;background:var(--green)}
  .back-photo{position:absolute;right:0;top:0;width:270px;height:290px;
    background:radial-gradient(circle at 35% 35%,#b4572c 0 18%,transparent 19%),
               radial-gradient(circle at 60% 75%,#a2442b 0 18%,transparent 19%),
               radial-gradient(circle at 80% 20%,#8a6a4a 0 14%,transparent 15%),
               linear-gradient(160deg,#d9d9d6,#bfc0bc)}
  .no-contract{position:absolute;right:10px;top:300px;width:260px;height:220px;background:var(--green);color:#fff;text-align:center;padding:16px 14px}
  .no-contract h2{font-size:21px;font-weight:700;line-height:1.3}
  .no-contract p{font-size:14px;line-height:1.45;margin-top:6px}
  .no-contract p + p{margin-top:22px}
</style>
</head>
<body>

<section class="flyer flyer--front">
  <div class="front-photo" role="img" aria-label="Foto einer Bowl mit Lachs, Reis, Edamame, Seetang und Tempeh"></div>
  <div class="brand">
    <div class="brand__name">pilvo bringt's</div>
    <div class="brand__tagline">ihr mobiler Mittagstisch aus Gägelow</div>
  </div>
  <div class="front-phone">03841/5550127</div>
  <div class="front-mail">
    <svg width="30" height="23" viewBox="0 0 34 26"><rect width="34" height="26" rx="2" fill="#3fa13a"/><path d="M2 3 L17 15 L32 3" stroke="#fff" stroke-width="3" fill="none"/></svg>
    pilvo@postfeld.de
  </div>
  <div class="price-badge">
    <div class="price-badge__price">6,00€/Menü</div>
    <div class="price-badge__note">inkl. Nachtisch und Lieferung</div>
    <div class="price-badge__extra">1 Stück selbstgebackenen Kuchen liefern wir ihnen gerne für <b>1,50€</b> mit dazu</div>
  </div>
</section>

<section class="flyer flyer--back">
  <div class="back-text">
    <p>Wir liefern ihnen gerne ihr Wunschmenü in unseren Thermoboxen zu ihnen nachhause oder auch ins Büro oder ihren Arbeitsplatz. Sie haben täglich die Wahl zwischen <span class="hl">3 Menüs inkl. Nachtisch</span></p>
    <p><strong>Bei der Bezahlung haben Sie die Wahl zwischen :</strong></p>
    <ul class="payment">
      <li><span class="hl">Barzahlung:</span> immer Montags im Vorraus beim Fahrer gegen Erhalt der Wochenrechnung</li>
      <li><span class="hl">Monatsrechnung:</span> am Ende des Monats wird ihnen eine Rechnung für den jeweiligen. Monat ausgestellt die Sie dann einfach überweisen.</li>
    </ul>
    <p>Auslieferung erfolgt von Montag - Samstag<br>zwischen 10.30Uhr und 12.30Uhr</p>
    <div class="area-band">Derzeitiges Auslieferungsgebiet Gägelow-Proseken-Barnekow-Zierow-Gressow-Stofferdorf- Woltersdorf- Wismar- Neuburg -Hornstorf -Kritzow auch weitere möglich</div>
    <p>Fordern sie noch heute einen Speiseplan von uns an, und lassen Sie sich von unseren täglich frisch zubereiteten Speisen überzeugen.</p>
  </div>
  <div class="back-brand"><i></i>pilvo</div>
  <div class="hotline">
    <div class="hotline__label">Bestellhotline :</div>
    <div class="hotline__row">
      <span><svg width="16" height="16" viewBox="0 0 24 24"><path fill="#3fa13a" d="M6.6 10.8a15 15 0 0 0 6.6 6.6l2.2-2.2c.3-.3.7-.4 1-.2 1.1.4 2.3.6 3.6.6.6 0 1 .4 1 1V20c0 .6-.4 1-1 1A17 17 0 0 1 3 4c0-.6.4-1 1-1h3.5c.6 0 1 .4 1 1 0 1.3.2 2.5.6 3.6.1.3 0 .7-.2 1z"/></svg>03841/5550127</span>
      <span><svg width="18" height="14" viewBox="0 0 34 26"><rect width="34" height="26" rx="2" fill="#3fa13a"/><path d="M2 3 L17 15 L32 3" stroke="#fff" stroke-width="3" fill="none"/></svg>pilvo@postfeld.de</span>
    </div>
  </div>
  <div class="back-photo" role="img" aria-label="Foto von Schmorgerichten in schwarzen Schalen mit Gewürzen und Kräutern"></div>
  <div class="no-contract">
    <h2>Keine<br>Vertragsbindung!!</h2>
    <p>d.h. Sollte es ihnen nicht gefallen können Sie jederzeit wieder abbestellen</p>
    <p>An-und Abbestellungen sind täglich bis 10.00Uhr möglich</p>
  </div>
</section>

</body>
</html>
```